Trade show flier

Need a two sided flier for a trade show that will go with the trade show banner you are designing for us. We have included some information we would like to see o the flier. We do need to work on the content. If you can start a design, we can work on the content. This must be done by 3/12/2018

Manufacturing companies

Trade

```html
<!DOCTYPE html>
<html lang="en">
<head>
<meta charset="utf-8">
<title>Linkwise Systems — Company Profile Flier</title>
<link href="https://fonts.googleapis.com/css2?family=Bebas+Neue&family=Didact+Gothic&family=Questrial&display=swap" rel="stylesheet">
<style>
  :root {
    --bg: #232323;
    --paper: #ffffff;
    --brand-blue: #2a72b8;
    --soft-blue: #86a8d0;
    --navy: #263f68;
    --ink: #222a33;
    --panel-grey: #f2f2f2;
    --charcoal: #3a3a3c;
    --photo-dark: #1c1c1c;
    --photo-mid: #5a5a5a;
    --badge: #c9ccd1;
  }
  * { margin: 0; padding: 0; box-sizing: border-box; }
  html, body { width: 1200px; height: 831px; overflow: hidden; background: var(--bg); }
  .stage {
    position: absolute; left: 0; top: 0;
    width: 1480px; height: 1025px;
    transform: scale(0.81081); transform-origin: 0 0;
    font-family: "Didact Gothic", sans-serif;
  }
  .abs { position: absolute; }

  /* Front side */
  .front { left: 98px; top: 87px; width: 602px; height: 849px; background: var(--paper); }
  .front-photo {
    left: 8px; top: 8px; width: 587px; height: 833px;
    background: radial-gradient(ellipse at 65% 40%, var(--photo-mid) 0%, #383838 45%, var(--photo-dark) 100%);
  }
  .front-frame { left: 24px; top: 113px; width: 556px; height: 712px; border: 1px solid rgba(255,255,255,.85); border-top: none; }
  .brand-band {
    left: 24px; top: 23px; width: 556px; height: 90px;
    background: rgba(255,255,255,.9);
    display: flex; align-items: center; justify-content: center; gap: 12px;
  }
  .brand-mark { width: 38px; height: 38px; border-radius: 50%; background: var(--brand-blue); }
  .brand-name { font-family: "Questrial", sans-serif; font-size: 30px; color: var(--brand-blue); letter-spacing: 1px; }
  .title {
    left: 88px; top: 282px;
    font-family: "Bebas Neue", sans-serif; color: #fff;
    font-size: 104px; line-height: 82px; letter-spacing: 1px;
  }
  .intro {
    left: 88px; top: 481px; width: 287px; height: 169px;
    background: var(--brand-blue); color: #fff;
    padding: 20px 18px; font-size: 10.5px; line-height: 18px; text-align: justify; letter-spacing: .8px;
  }
  .statement { left: 395px; width: 165px; color: #fff; }
  .statement h2 { font-family: "Questrial", sans-serif; font-weight: 400; font-size: 18px; letter-spacing: 3.5px; margin-bottom: 8px; }
  .statement p { font-size: 10.5px; line-height: 18px; letter-spacing: .8px; }
  .vision { top: 509px; }
  .mission { top: 665px; }
  .divider { left: 395px; top: 650px; width: 105px; height: 1px; background: rgba(255,255,255,.7); }

  /* Back side */
  .back { left: 776px; top: 88px; width: 602px; height: 850px; background: var(--paper); }
  .col-head {
    top: 8px; height: 66px; color: #fff;
    display: flex; align-items: center; justify-content: center; text-align: center;
    font-family: "Questrial", sans-serif; font-size: 15px; letter-spacing: 1.6px; line-height: 18px;
  }
  .head-services { left: 39px; width: 261px; background: var(--brand-blue); }
  .head-included { left: 300px; width: 262px; background: var(--soft-blue); }
  .services-panel { left: 39px; top: 74px; width: 261px; height: 563px; background: var(--panel-grey); }
  .list { list-style: none; display: flex; flex-direction: column; gap: 14px; color: var(--ink); font-size: 10px; line-height: 14px; }
  .list li { position: relative; }
  .list li::before { content: ""; position: absolute; left: -9px; top: 5px; width: 4px; height: 4px; border-radius: 50%; background: var(--brand-blue); }
  .list-services { left: 64px; top: 107px; width: 210px; }
  .list-included { left: 337px; top: 107px; width: 210px; }
  .promise {
    left: 8px; top: 637px; width: 587px; height: 80px;
    background: linear-gradient(120deg, #2d4a78 0%, var(--navy) 50%, #1f355a 100%);
    color: #fff; font-size: 11px; font-weight: 700; line-height: 20px; padding: 16px 0 0 55px;
    -webkit-text-stroke: .2px #fff;
  }
  .partners-label {
    left: 32px; top: 707px; width: 283px; height: 34px; background: var(--charcoal);
    color: #fff; font-family: "Questrial", sans-serif; font-size: 14px; letter-spacing: 1px;
    display: flex; align-items: center; justify-content: center;
  }
  .partner-badge { height: 22px; border-radius: 3px; background: var(--badge); }
</style>
</head>
<body>
<div class="stage">

  <section class="front abs" aria-label="Front side">
    <div class="front-photo abs" role="img" aria-label="Black and white photo of a team collaborating over plans at a desk"></div>
    <div class="brand-band abs">
      <span class="brand-mark"></span>
      <span class="brand-name">linkwise systems</span>
    </div>
    <div class="front-frame abs"></div>
    <h1 class="title abs">Company<br>Profile</h1>
    <p class="intro abs">Established in 2006, Linkwise Systems is a Managed IT Service firm providing exceptional IT consultation and support for businesses in the California with 20 – 1000 employees. Our personable, reliable and professional team empowers our clients to make their IT infrastructure a strategic asset.</p>
    <div class="statement vision abs">
      <h2>OUR VISION</h2>
      <p>To provide a customer experience that provides value and enables technology collaboration effortlessly.</p>
    </div>
    <div class="divider abs"></div>
    <div class="statement mission abs">
      <h2>OUR MISSION</h2>
      <p>Innovative collaboration to improve business process by leveraging technology that empowers organizations to implement a roadmap to success.</p>
    </div>
  </section>

  <section class="back abs" aria-label="Back side">
    <div class="col-head head-services abs">SERVICES</div>
    <div class="col-head head-included abs">OUR COMMON GROUND<br>MANAGED SERVICES<br>SUPPORT INCLUDE</div>
    <div class="services-panel abs"></div>

    <ul class="list list-services abs">
      <li>Managed Services – Proactive support,<br>remediation and maintenance of your<br>technology infrastructure, 24/7.</li>
      <li>Backup and Business Continuity –<br>Secure your data while minimizing<br>downtime.</li>
      <li>Virtualization – Increase IT flexibility and<br>scalability while minimizing hardware<br>resources.</li>
      <li>Voice Collaboration – Voice-over-IP<br>(VOIP) Design and Deployment.</li>
      <li>Cloud Services – Leverage cloud support<br>services for remote access and or<br>business continuity.</li>
      <li>Security Services – Multi-layered<br>approach to addressing your network<br>security.</li>
      <li>Wireless Services – Secure connectivity<br>and centralized management for wireless<br>endpoint devices.</li>
      <li>Procurement Services – Procurement of<br>industry standard business class product.</li>
      <li>Project Collaboration – Strategic<br>technology roadmaps that address<br>company business goals.</li>
      <li>Surveillance Services - Intelligent<br>network security video solutions.</li>
    </ul>

    <ul class="list list-included abs">
      <li>Team of industry certified Network<br>Engineers</li>
      <li>Remote support (Weekdays 7am – 6pm)</li>
      <li>Onsite support (Weekdays 7am – 6pm)</li>
      <li>24x7 network monitoring and<br>remediation</li>
      <li>Daily proactive maintenance</li>
      <li>Managed antivirus software</li>
      <li>Managed ransomware protection</li>
      <li>Ticketing portal to track open tickets and<br>resolutions</li>
      <li>Vendor management</li>
      <li>Network Documentation Management</li>
      <li>Software License Management</li>
      <li>Technology procurement</li>
      <li>Monitoring of existing backup systems<br>and data recovery</li>
      <li>Business continuity planning</li>
      <li>Network and data security planning and<br>testing</li>
      <li>Quarterly IT meetings</li>
    </ul>

    <p class="promise abs">We provide a great customer service experience with a simplified, cost-effective approach to<br>IT that leverages certified technical professionals with industry standard skills and knowledge.</p>
    <div class="partners-label abs">OUR TECHNOLOGY PARTNERS</div>

    <div class="partner-badge abs" style="left:66px;top:761px;width:110px;" aria-label="Partner badge"></div>
    <div class="partner-badge abs" style="left:213px;top:761px;width:72px;" aria-label="Partner badge"></div>
    <div class="partner-badge abs" style="left:338px;top:761px;width:64px;" aria-label="Partner badge"></div>
    <div class="partner-badge abs" style="left:443px;top:761px;width:94px;" aria-label="Partner badge"></div>
    <div class="partner-badge abs" style="left:66px;top:800px;width:84px;" aria-label="Partner badge"></div>
    <div class="partner-badge abs" style="left:213px;top:798px;width:72px;" aria-label="Partner badge"></div>
    <div class="partner-badge abs" style="left:333px;top:800px;width:76px;" aria-label="Partner badge"></div>
    <div class="partner-badge abs" style="left:456px;top:796px;width:76px;" aria-label="Partner badge"></div>
  </section>

</div>
</body>
</html>
```